New signage for workshop frontage. Tarnell Welding & Repair is the company name. Looking for a cool font, metal fabrication is the trade. Also use TWAR as the logo

```html
<!DOCTYPE html>
<html lang="en">
<head>
<meta charset="utf-8">
<title>Tarnell Welding &amp; Repair – Workshop Signage</title>
<link rel="stylesheet" href="https://fonts.googleapis.com/css2?family=Anton&family=Poppins:wght@700&display=swap">
<style>
  :root {
    --backdrop: #dadada;
    --blue-bright: #00c9ef;
    --blue-mid: #04a6e6;
    --blue-deep: #0a78d6;
    --ink: #1c1b1d;
    --white: #ffffff;
    --brand-blue: #1670b9;
    --badge-navy: #0f2542;
    --badge-blue: #1662aa;
    --plate-dark: #2e2e30;
    --plate-light: #5a5a5d;
    --plate-rim: #c9c9cc;
    --divider: #e6e6e6;
  }
  html, body {
    margin: 0;
    width: 1200px;
    height: 1200px;
    overflow: hidden;
    background: var(--backdrop);
  }
  .sign {
    position: absolute;
    left: 0;
    top: 200px;
    width: 1200px;
    height: 800px;
    display: block;
  }
  .headline { font-family: "Anton", "Impact", sans-serif; }
  .headline--light { fill: var(--white); }
  .headline--dark { fill: var(--ink); }
  .intro { font-family: "Poppins", sans-serif; font-weight: 700; fill: var(--white); }
  .service-label { font-family: "Anton", "Impact", sans-serif; fill: var(--ink); }
  .plate-text { font-family: "Poppins", sans-serif; font-weight: 700; fill: var(--white); }
  .brand-name { font-family: "Anton", "Impact", sans-serif; fill: var(--ink); }
  .web-address { font-family: "Anton", "Impact", sans-serif; fill: var(--ink); }
  .web-address .web-domain { fill: var(--brand-blue); }
</style>
</head>
<body>
<svg class="sign" viewBox="0 0 1200 800" xmlns="http://www.w3.org/2000/svg">
  <defs>
    <linearGradient id="blueBase" x1="0" y1="0" x2="0" y2="1">
      <stop offset="0" stop-color="var(--blue-mid)"/>
      <stop offset="1" stop-color="var(--blue-deep)"/>
    </linearGradient>
    <radialGradient id="blueGlow" cx="0.28" cy="0.08" r="0.6">
      <stop offset="0" stop-color="var(--blue-bright)" stop-opacity="1"/>
      <stop offset="1" stop-color="var(--blue-bright)" stop-opacity="0"/>
    </radialGradient>
    <linearGradient id="plateFill" x1="0" y1="0" x2="1" y2="1">
      <stop offset="0" stop-color="var(--plate-dark)"/>
      <stop offset="0.45" stop-color="var(--plate-light)"/>
      <stop offset="1" stop-color="var(--plate-dark)"/>
    </linearGradient>
  </defs>

  <!-- backgrounds -->
  <rect class="sign-base" x="0" y="0" width="1200" height="800" fill="var(--white)"/>
  <rect class="hero-band" x="0" y="0" width="1200" height="533" fill="url(#blueBase)"/>
  <rect class="hero-glow" x="0" y="0" width="1200" height="533" fill="url(#blueGlow)"/>

  <!-- headline -->
  <text class="headline headline--light" x="81" y="227" font-size="170" textLength="1037" lengthAdjust="spacingAndGlyphs">ENGINEERING &amp;</text>
  <text class="headline headline--dark" x="81" y="400" font-size="170" textLength="866" lengthAdjust="spacingAndGlyphs">FABRICATION</text>

  <text class="intro" x="81" y="484" font-size="47" textLength="352" lengthAdjust="spacingAndGlyphs">SPECIALISTS IN</text>

  <!-- services -->
  <g class="service-dividers" stroke="var(--divider)" stroke-width="2">
    <line x1="185" y1="542" x2="185" y2="612"/>
    <line x1="411" y1="542" x2="411" y2="612"/>
    <line x1="605" y1="542" x2="605" y2="612"/>
  </g>

  <g class="tick-badges">
    <g transform="translate(116 536)">
      <circle r="33" fill="var(--white)"/><circle r="30" fill="var(--badge-navy)"/><circle r="22" fill="var(--badge-blue)"/>
      <path d="M-11 1 L-3 9 L12 -8" fill="none" stroke="var(--white)" stroke-width="6" stroke-linecap="round" stroke-linejoin="round"/>
    </g>
    <g transform="translate(298 536)">
      <circle r="33" fill="var(--white)"/><circle r="30" fill="var(--badge-navy)"/><circle r="22" fill="var(--badge-blue)"/>
      <path d="M-11 1 L-3 9 L12 -8" fill="none" stroke="var(--white)" stroke-width="6" stroke-linecap="round" stroke-linejoin="round"/>
    </g>
    <g transform="translate(505 536)">
      <circle r="33" fill="var(--white)"/><circle r="30" fill="var(--badge-navy)"/><circle r="22" fill="var(--badge-blue)"/>
      <path d="M-11 1 L-3 9 L12 -8" fill="none" stroke="var(--white)" stroke-width="6" stroke-linecap="round" stroke-linejoin="round"/>
    </g>
    <g transform="translate(706 536)">
      <circle r="33" fill="var(--white)"/><circle r="30" fill="var(--badge-navy)"/><circle r="22" fill="var(--badge-blue)"/>
      <path d="M-11 1 L-3 9 L12 -8" fill="none" stroke="var(--white)" stroke-width="6" stroke-linecap="round" stroke-linejoin="round"/>
    </g>
  </g>

  <text class="service-label" x="81" y="607" font-size="26" textLength="74" lengthAdjust="spacingAndGlyphs">DESIGN</text>
  <text class="service-label" x="211" y="607" font-size="26" textLength="175" lengthAdjust="spacingAndGlyphs">MANUFACTURING</text>
  <text class="service-label" x="436" y="607" font-size="26" textLength="140" lengthAdjust="spacingAndGlyphs">INSTALLATION</text>
  <text class="service-label" x="633" y="607" font-size="26" textLength="148" lengthAdjust="spacingAndGlyphs">MAINTENANCE</text>

  <!-- sector plate -->
  <g class="sector-plate">
    <rect x="817" y="458" width="383" height="151" fill="var(--plate-rim)"/>
    <rect x="821" y="462" width="379" height="143" fill="url(#plateFill)"/>
    <g class="plate-screws" stroke="var(--plate-rim)" stroke-width="1.5" fill="var(--plate-dark)">
      <circle cx="846" cy="484" r="6"/><path d="M842 480 L850 488 M850 480 L842 488"/>
      <circle cx="1178" cy="484" r="6"/><path d="M1174 480 L1182 488 M1182 480 L1174 488"/>
      <circle cx="846" cy="582" r="6"/><path d="M842 578 L850 586 M850 578 L842 586"/>
      <circle cx="1178" cy="582" r="6"/><path d="M1174 578 L1182 586 M1182 578 L1174 586"/>
    </g>
    <text class="plate-text" x="869" y="513" font-size="27" textLength="224" lengthAdjust="spacingAndGlyphs">OF INDUSTRIAL</text>
    <text class="plate-text" x="869" y="543" font-size="27" textLength="206" lengthAdjust="spacingAndGlyphs">COMMERCIAL</text>
    <text class="plate-text" x="869" y="573" font-size="27" textLength="266" lengthAdjust="spacingAndGlyphs">INFRASTRUCTURE</text>
  </g>

  <!-- brand and web -->
  <text class="brand-name" x="81" y="731" font-size="81" textLength="225" lengthAdjust="spacingAndGlyphs">TWAR</text>

  <text class="web-address" x="405" y="729" font-size="37" textLength="725" lengthAdjust="spacingAndGlyphs" letter-spacing="4">WWW.<tspan class="web-domain">TARNELLWELDING</tspan>.NET.AU</text>
</svg>
</body>
</html>
```